Business Card Design Project for New Home Builder

Double sided card,
Larger logo on 1 side with small quote, More than walls, it's where you belong, across the bottom. Matt Red base, White logo, black quote??

other side, ,
Its your Home LHS. Smaller logo RHS with.
Details below.

"Licensed Builder" Logo Font

Derek Hollins

PO Box 7384 Mildura VIC 3502
Mobile 0427 318950 / Phone 03 50871 639 / Fax 03 50871 982
email DerekH@wvbuilds.net.au
Vic Building Practitioner DB-U 8147 Vic Commercial Builder CB-U 5093
NSW Contractor Reg 67318C

Target Market(s)

New Home Buyers

Industry/Entity Type

Business

Requirements
Must have
• Sharp detail, Red Black & White colourings.
Should not have
• Any new colours

```html
<!DOCTYPE html>
<html lang="en">
<head>
<meta charset="utf-8">
<title>Westvale Homes – Business Card</title>
<link rel="stylesheet" href="https://fonts.googleapis.com/css2?family=Open+Sans:wght@400;600&display=swap">
<style>
  :root {
    --brand-red: #e31e24;
    --paper: #ffffff;
    --ink: #2b2b2b;
    --ink-soft: #8a8a8a;
    --backdrop: #ececec;
  }
  * { box-sizing: border-box; margin: 0; padding: 0; }
  html, body {
    width: 1155px; height: 1200px; overflow: hidden;
    background: var(--backdrop);
    font-family: "Open Sans", Arial, sans-serif;
  }
  .sheet {
    width: 1155px; height: 1200px;
    display: flex; flex-direction: column; align-items: center; justify-content: center;
    gap: 50px;
  }
  .card {
    position: relative; width: 860px; height: 528px; overflow: hidden;
    box-shadow: 0 2px 10px rgba(0,0,0,0.12);
  }

  /* Details side */
  .card--details { background: var(--paper); }
  .card--details .base-band {
    position: absolute; left: 0; right: 0; bottom: 0; height: 62px; background: var(--brand-red);
  }
  .identity {
    position: absolute; left: 60px; width: 380px; top: 0; bottom: 62px;
    display: flex; flex-direction: column; align-items: center;
  }
  .wordmark {
    display: flex; align-items: center; gap: 10px;
    font-weight: 600; letter-spacing: 1px; white-space: nowrap;
  }
  .card--details .wordmark { margin-top: 138px; font-size: 30px; color: var(--ink); }
  .wordmark .mark { width: 18px; height: 18px; background: var(--brand-red); }
  .holder { margin-top: 100px; text-align: center; }
  .holder-name { font-size: 32px; font-weight: 400; color: var(--ink); letter-spacing: 0.5px; line-height: 40px; }
  .holder-role { font-size: 18px; color: var(--brand-red); line-height: 26px; }

  .contact { position: absolute; right: 52px; top: 140px; text-align: right; font-size: 15px; color: var(--ink-soft); }
  .contact p { line-height: 24px; white-space: nowrap; }
  .contact .post { color: var(--brand-red); font-weight: 600; margin: 18px 0 44px; }
  .contact .line { display: flex; justify-content: flex-end; align-items: center; gap: 8px; }
  .contact .icon { width: 14px; height: 14px; fill: var(--brand-red); flex: none; }

  /* Brand side */
  .card--brand { background: var(--brand-red); }
  .card--brand .wordmark {
    position: absolute; left: 0; right: 0; top: 190px; justify-content: center;
    font-size: 58px; color: var(--paper); letter-spacing: 2px;
  }
  .tagline-band {
    position: absolute; left: 0; right: 0; top: 418px; height: 36px; background: var(--paper);
    display: flex; align-items: center; justify-content: center;
    font-size: 15px; color: var(--ink-soft); white-space: nowrap;
  }
</style>
</head>
<body>
<main class="sheet">

  <section class="card card--details" aria-label="Card details side">
    <div class="identity">
      <div class="wordmark"><span class="mark"></span>WESTVALE HOMES</div>
      <div class="holder">
        <h1 class="holder-name">DEREK HOLLINS</h1>
        <p class="holder-role">Licensed Builder</p>
      </div>
    </div>
    <div class="contact">
      <p>Vic Building Practitioner DB-U 8147</p>
      <p>Vic Commercial Builder CB-U 5093</p>
      <p>NSW Contractor Reg 67318C</p>
      <p class="post">PO Box 7384 Lakeview VIC 3588</p>
      <p class="line">0427 318950
        <svg class="icon" viewBox="0 0 14 14"><rect x="3" y="0" width="8" height="14" rx="2"/><rect x="5" y="2" width="4" height="8" fill="#fff"/></svg></p>
      <p class="line">03 50871 639
        <svg class="icon" viewBox="0 0 14 14"><path d="M3 1c1 0 2 2 2 3s-1 1-1 2 3 4 4 4 1-1 2-1 3 1 3 2-1 2-2 2C6 13 1 8 1 3c0-1 1-2 2-2z"/></svg></p>
      <p class="line">03 50871 982
        <svg class="icon" viewBox="0 0 14 14"><rect x="3" y="0" width="8" height="5"/><rect x="1" y="5" width="12" height="7" rx="1"/><rect x="3" y="10" width="8" height="4"/></svg></p>
      <p class="line">email DerekH@wvbuilds.net.au
        <svg class="icon" viewBox="0 0 14 14"><circle cx="7" cy="7" r="7"/><path d="M3 5h8v5H3z M3 5l4 3 4-3" fill="none" stroke="#fff" stroke-width="1"/></svg></p>
      <p class="line">www.wvbuilds.net.au
        <svg class="icon" viewBox="0 0 14 14"><circle cx="7" cy="7" r="7"/></svg></p>
    </div>
    <div class="base-band"></div>
  </section>

  <section class="card card--brand" aria-label="Card brand side">
    <div class="wordmark">WESTVALE HOMES</div>
    <div class="tagline-band">More than walls, it's where you belong</div>
  </section>

</main>
</body>
</html>
```